Harrowvane Business Card

Looking for a new business Card layout for our company, harrowvane.

Standard Business Card , Name, email, phone, website. www.harrowvane.com

```html
<!DOCTYPE html>
<html lang="en">
<head>
<meta charset="UTF-8">
<title>Harrowvane Business Card</title>
<link rel="stylesheet" href="https://fonts.googleapis.com/css2?family=Montserrat:wght@500;700;800&family=Roboto:wght@400&display=swap">
<style>
  :root {
    --sky: #45b4dc;
    --sky-bright: #3fbbe6;
    --slate: #5a6680;
    --slate-deep: #525d76;
    --ink: #5b6477;
    --paper: #ffffff;
    --backdrop: #2a2a2c;
  }
  * { box-sizing: border-box; margin: 0; padding: 0; }
  html, body {
    width: 1200px; height: 880px; overflow: hidden;
    background: var(--backdrop);
  }
  .canvas {
    width: 1200px; height: 880px;
    display: flex; flex-direction: column;
    align-items: center; justify-content: center; gap: 56px;
  }
  .card {
    position: relative;
    width: 560px; height: 320px;
    border-radius: 18px;
    overflow: hidden;
    box-shadow: 0 14px 30px rgba(0,0,0,0.45);
  }

  /* Front */
  .card--front {
    background: linear-gradient(180deg, var(--sky-bright) 0%, var(--slate) 28%, var(--slate-deep) 60%, var(--slate) 80%, var(--sky-bright) 100%);
    color: var(--paper);
    display: flex; flex-direction: column; align-items: center; justify-content: center;
  }
  .front-brand {
    display: flex; align-items: center; gap: 14px;
    font-family: "Montserrat", sans-serif; font-weight: 800;
    font-size: 46px; letter-spacing: 1px; text-transform: uppercase;
  }
  .brand-dot {
    width: 22px; height: 22px; border-radius: 50%;
    background: var(--paper);
  }
  .front-web {
    margin-top: 22px;
    font-family: "Roboto", sans-serif; font-size: 15px;
    opacity: 0.9; letter-spacing: 0.5px;
  }

  /* Back */
  .card--back { background: var(--paper); }
  .back-decor {
    position: absolute; right: 0; top: 0;
    width: 200px; height: 220px;
    border-bottom-left-radius: 120px;
    background: linear-gradient(150deg, var(--slate) 0%, var(--sky) 70%);
  }
  .back-content {
    position: absolute; left: 44px; top: 66px;
    width: 300px;
  }
  .back-brand {
    font-family: "Montserrat", sans-serif; font-weight: 800;
    font-size: 33px; color: var(--sky);
    text-transform: uppercase; letter-spacing: 0.3px;
    white-space: nowrap;
  }
  .person { margin-top: 24px; }
  .person-name {
    font-family: "Montserrat", sans-serif; font-weight: 700;
    font-size: 21px; color: var(--sky);
  }
  .person-role {
    font-family: "Roboto", sans-serif; font-size: 16px; color: var(--ink);
  }
  .contact { list-style: none; margin-top: 14px; }
  .contact li {
    display: flex; align-items: center; gap: 10px;
    font-family: "Roboto", sans-serif; font-size: 15px; color: var(--ink);
    line-height: 23px;
  }
  .contact svg { width: 14px; height: 14px; flex: none; }
  .contact .accent { color: var(--sky); }
  .address {
    margin-top: 10px;
    font-family: "Roboto", sans-serif; font-size: 15px; color: var(--ink);
    white-space: nowrap;
  }
</style>
</head>
<body>
<main class="canvas">
  <section class="card card--front">
    <div class="front-brand"><span class="brand-dot"></span>Harrowvane</div>
    <p class="front-web">www.harrowvane.com</p>
  </section>

  <section class="card card--back">
    <div class="back-decor" role="img" aria-label="Brand decoration in blue and slate"></div>
    <div class="back-content">
      <h1 class="back-brand">Harrowvane</h1>
      <div class="person">
        <p class="person-name">Marcus Ellery</p>
        <p class="person-role">Manager</p>
      </div>
      <ul class="contact">
        <li>
          <svg viewBox="0 0 16 16"><path d="M4 1.5 6 4.5 4.8 6.2c.8 1.9 2.5 3.9 4.6 5L11 10l3 2-1.2 2.3C7.5 14 2.3 8.6 1.8 3.2Z" fill="var(--sky)"/></svg>
          555-204-7781
        </li>
        <li>
          <svg viewBox="0 0 16 16"><rect x="1.5" y="3.5" width="13" height="9" rx="1" fill="none" stroke="var(--sky)" stroke-width="1.5"/><path d="M2 4l6 5 6-5" fill="none" stroke="var(--sky)" stroke-width="1.5"/></svg>
          contact@harrowvane.com
        </li>
        <li>
          <svg viewBox="0 0 16 16"><circle cx="8" cy="8" r="6.5" fill="none" stroke="var(--sky)" stroke-width="1.4"/><ellipse cx="8" cy="8" rx="2.8" ry="6.5" fill="none" stroke="var(--sky)" stroke-width="1.2"/><path d="M1.5 8h13M2.5 5h11M2.5 11h11" stroke="var(--sky)" stroke-width="1.1"/></svg>
          <span>www.<span class="accent">harrowvane</span>.com</span>
        </li>
      </ul>
      <p class="address">Your address, city, state, ZIP 0000</p>
    </div>
  </section>
</main>
</body>
</html>
```